IT Company based on Biology Business Needs a PowerPoint Design

We need a powerpoint design for a new company called 'Tall FERN'. We develop the machine learning solutions especially focused on deep learning algorithms for biology industry. Our initial product is a vision detection on biological images to help doctors diagnose the symptoms. We would like to see designs that use the color green.

Industry/Entity Type

Biotechnology

Requirements
Nice to have
• Lots of slide templates with company logo's look and feel

```html
<!DOCTYPE html>
<html lang="en">
<head>
<meta charset="utf-8">
<title>Tall FERN – Presentation Templates</title>
<link href="https://fonts.googleapis.com/css2?family=Open+Sans:ital,wght@0,300;0,400;0,600;1,700&family=Roboto+Condensed:wght@400&display=swap" rel="stylesheet">
<style>
:root{
  --bg:#dcdddf;
  --green:#6cbe45;
  --green-light:#8fd05f;
  --green-dark:#1a9340;
  --green-deep:#0d6b34;
  --gray:#8c8c8c;
  --gray-light:#b5b5b5;
  --text:#6f6f6f;
  --white:#ffffff;
}
*{margin:0;padding:0;box-sizing:border-box}
html,body{width:1200px;height:900px;overflow:hidden;background:var(--bg);font-family:"Open Sans",sans-serif;color:var(--text)}
.deck{position:relative;width:1200px;height:900px}
.slide{position:absolute;width:362px;height:203px;background:var(--white);overflow:hidden}
.c1{left:38px}.c2{left:409px}.c3{left:781px}
.r1{top:34px}.r2{top:244px}.r3{top:456px}.r4{top:666px}
.abs{position:absolute}
.title{position:absolute;left:12px;top:10px;right:12px;font-weight:300;font-size:9px;color:var(--green);letter-spacing:.2px;border-bottom:.6px solid var(--gray-light);padding-bottom:1px}
.body{font-size:4.6px;line-height:7.8px;color:var(--text);text-align:justify}
.brand{font-family:"Open Sans",sans-serif;font-weight:600;color:var(--green);display:flex;align-items:center;white-space:nowrap}
.brand .mark{background:var(--green);display:inline-block}
.foot-brand{position:absolute;left:5px;bottom:7px;font-size:5px}
.foot-brand .mark{width:4px;height:4px;margin-right:2px}
.foot-line{position:absolute;left:0;bottom:2px;width:310px;height:2px;background:var(--gray-light)}
.foot-tab{position:absolute;right:0;bottom:0;width:64px;height:5px;background:var(--green);clip-path:polygon(8% 0,100% 0,100% 100%,0 100%);font-size:3px;color:var(--white);text-align:right;padding-right:6px;line-height:5px}
.photo{position:absolute}
/* welcome */
.welcome .brand{position:absolute;left:34px;top:36px;font-size:17px;font-weight:400;letter-spacing:-.5px}
.welcome .brand .mark{width:8px;height:8px;margin-right:5px}
.welcome h1{position:absolute;right:24px;top:94px;font-family:"Roboto Condensed",sans-serif;font-weight:400;font-size:17px;color:var(--white)}
.welcome .sub{position:absolute;right:24px;top:115px;font-size:8px;font-weight:300;letter-spacing:2.3px;color:var(--white)}
.welcome .date{position:absolute;right:24px;top:131px;font-size:4.8px;color:var(--white)}
.welcome .legal{position:absolute;left:19px;top:182px;font-size:3.4px;line-height:4.6px;color:var(--gray)}
.welcome .rule{position:absolute;left:0;bottom:0;width:100%;height:2.5px;background:var(--green-dark)}
/* contents */
.contents{background:linear-gradient(120deg,#2c9a4d 0%,#14843d 45%,#0b6a33 100%)}
.contents .pre{position:absolute;left:37px;top:58px;font-size:5.5px;font-weight:300;color:var(--white)}
.contents h2{position:absolute;left:37px;top:66px;font-size:13px;font-weight:300;color:var(--white)}
.contents .bar{position:absolute;left:37px;top:86px;width:23px;height:1.5px;background:var(--white)}
.toc{position:absolute;left:165px;top:72px;list-style:none}
.toc li{position:relative;width:158px;height:12px;margin-bottom:6.6px}
.toc .num{position:absolute;left:0;top:-.5px;width:13px;height:13px;border-radius:50%;background:var(--green);border:1.2px solid #c9e9b6;color:var(--white);font-size:5px;text-align:center;line-height:10.5px}
.toc .item{position:absolute;left:6px;top:1px;right:0;height:10px;border-radius:2px;background:#e6e7e8;color:var(--text);font-size:5px;line-height:10px;padding-left:18px}
/* about team */
.about-a .panel{position:absolute;left:0;top:57px;width:118px;height:66px;background:var(--green);color:var(--white);font-size:4px;line-height:6.2px;padding:22px 10px 0 22px}
.about-a .body{position:absolute;left:115px;top:133px;width:231px}
/* about grid */
.tile{position:absolute;font-size:4.4px;line-height:7.6px}
.tile.g{background:var(--green);color:var(--white);font-size:5px;display:flex;align-items:center;padding-left:10px}
.tile.t{background:#7e7e7e;color:var(--white);padding:7px 9px 0 9px}
/* about columns */
.about-c .cap{position:absolute;left:22px;top:93px;width:74px;font-size:4.4px;line-height:7px;color:var(--green);text-align:center}
.about-c .col{position:absolute;top:50px;width:113px}
.about-c .col p{margin-bottom:8px}
/* market */
.pct{position:absolute;font-weight:600;color:var(--green-dark);font-size:10px}
.market .side{position:absolute;left:230px;top:91px;width:116px}
.market .side .lead{color:var(--green)}
/* bar chart */
.chart .year{position:absolute;top:144px;font-size:6px;color:var(--text)}
.legend{position:absolute;top:166px;width:70px;font-size:3.4px;line-height:4.6px}
.legend b{font-weight:400;font-size:4px;display:flex;align-items:center;margin-bottom:1px;color:var(--text)}
.legend b i{display:inline-block;width:4px;height:4px;margin-right:4px}
/* rings */
.ring-note{position:absolute;top:120px;width:80px;font-size:3.6px;line-height:5.6px;text-align:center;color:var(--gray)}
/* services */
.svc{position:absolute;top:54px;width:73px;height:112px;background:#8f8f8f}
.svc .top{height:46px;display:flex;align-items:center;justify-content:center}
.svc p{color:var(--white);font-size:4.2px;line-height:5.8px;text-align:center;padding:7px 6px 0}
/* image text */
.imgtext .left{position:absolute;left:0;top:0;width:155px;height:203px;background:var(--green)}
.imgtext h3{position:absolute;left:22px;top:19px;font-size:9px;font-weight:300;color:var(--white)}
.imgtext .body{position:absolute;left:22px;top:79px;width:124px;color:var(--white)}
.imgtext .foot-brand{color:var(--white)}
.imgtext .foot-brand .mark{background:var(--white)}
/* section */
.section{background:radial-gradient(circle at 30% 40%,#9fd46e 0%,#7cc44d 45%,#5fae38 100%)}
.section .icon{position:absolute;left:160px;top:86px;width:40px;height:40px;border-radius:50%;background:var(--white);color:var(--green);font-style:italic;font-weight:700;font-size:30px;text-align:center;line-height:40px}
.section .line{position:absolute;left:133px;top:134px;width:95px;height:.8px;background:rgba(255,255,255,.8)}
.section h4{position:absolute;left:0;width:100%;top:140px;text-align:center;font-weight:300;font-size:10px;color:var(--white)}
/* contact */
.contact .brand{position:absolute;left:34px;top:37px;font-size:15px;font-weight:400}
.contact .brand .mark{width:7px;height:7px;margin-right:5px}
.contact .info{position:absolute;left:0;top:173px;width:100%;height:30px;background:var(--green-dark);display:flex;align-items:center;gap:26px;padding-left:31px;font-size:5px;color:var(--white)}
.contact .info span{display:flex;align-items:center;gap:4px}
.contact .info i{width:8px;height:8px;border-radius:50%;background:var(--green-light);display:inline-block}
</style>
</head>
<body>
<main class="deck">

  <!-- Welcome -->
  <section class="slide welcome c1 r1">
    <div class="brand"><span class="mark"></span>Tall FERN</div>
    <svg class="abs" style="left:0;top:0" width="362" height="203" role="img" aria-label="Green DNA helix artwork across the title band">
      <defs>
        <linearGradient id="wband" x1="0" x2="1" y1="0" y2="0">
          <stop offset="0" stop-color="#2f8a2a"/>
          <stop offset=".45" stop-color="#6cbe45"/>
          <stop offset="1" stop-color="#7cc84e"/>
        </linearGradient>
      </defs>
      <path d="M0 84 L160 84 Q200 84 228 70 Q252 60 290 60 L362 60 L362 158 L0 158 Z" fill="url(#wband)"/>
    </svg>
    <h1>WELCOME</h1>
    <div class="sub">TO OUR PRESENTATION</div>
    <div class="date">Ashford Vale, March 25, 2011</div>
    <p class="legal">© 2016 Tall Fern. All rights reserved. Contains confidential and proprietary information and may not be disclosed or<br>reproduced without the prior written consent of Tall Fern.</p>
    <div class="rule"></div>
  </section>

  <!-- Contents -->
  <section class="slide contents c2 r1" role="img" aria-label="Dark green background with faint DNA strand artwork">
    <div class="pre">TABLE OF</div>
    <h2>CONTENTS</h2>
    <div class="bar"></div>
    <ol class="toc">
      <li><span class="item">LOREM IPSUM DOLOR SIT MET</span><span class="num">1</span></li>
      <li><span class="item">LOREM IPSUM DOLOR SIT MET</span><span class="num">2</span></li>
      <li><span class="item">LOREM IPSUM DOLOR SIT MET</span><span class="num">3</span></li>
      <li><span class="item">LOREM IPSUM DOLOR SIT MET</span><span class="num">4</span></li>
      <li><span class="item">LOREM IPSUM DOLOR SIT MET</span><span class="num">5</span></li>
      <li><span class="item">LOREM IPSUM DOLOR SIT MET</span><span class="num">6</span></li>
    </ol>
  </section>

  <!-- About us: team -->
  <section class="slide about-a c3 r1">
    <div class="title">ABOUT US</div>
    <div class="panel">LOREM IPSUM DOLOR SIT MET<br>CONSECTUR ADIPISCING ELIT, SED<br>DO EIUSMOD TEMPOR INCIDIDUNT<br>UT LABORE ET DOLORE MAGNA</div>
    <div class="photo" style="left:118px;top:57px;width:244px;height:66px;background:linear-gradient(90deg,#dfe6ea,#c9d3d8 50%,#eef2f4)" role="img" aria-label="Team of medical staff in white coats"></div>
    <p class="body">Lorem ipsum dolor sit amet, consectetur adipiscing elit, sed do eiusmod tempor incididunt ut labore et dolore magna aliqua. Ut enim ad minim veniam, quis nostrud exercitation ullamco laboris nisi ut aliquip ex ea commodo consequat. Duis aute irure dolor in reprehenderit in voluptate velit esse cillum dolore eu fugiat nulla pariatur.</p>
    <div class="foot-brand brand"><span class="mark"></span>Tall FERN</div>
    <div class="foot-line"></div><div class="foot-tab">02</div>
  </section>

  <!-- About us: grid -->
  <section class="slide c1 r2">
    <div class="title">ABOUT US</div>
    <div class="tile g" style="left:28px;top:39px;width:78px;height:45px">LOREM IPSUM DOLOR</div>
    <div class="photo" style="left:106px;top:39px;width:74px;height:45px;background:linear-gradient(120deg,#e8e2dc,#cfc4ba)" role="img" aria-label="Doctor examining a child"></div>
    <div class="tile t" style="left:180px;top:39px;width:153px;height:45px">Lorem ipsum dolor sit amet, consectetur adipiscing elit, sed do eiusmod tempor incididunt ut labore et dolore magna aliqua. Ut enim ad minim veniam, quis nostrud exercitation</div>
    <div class="tile t" style="left:28px;top:84px;width:152px;height:45px">Lorem ipsum dolor sit amet, consectetur adipiscing elit, sed do eiusmod tempor incididunt ut labore et dolore magna aliqua. Ut enim ad minim veniam, quis nostrud exercitation</div>
    <div class="tile g" style="left:180px;top:84px;width:79px;height:45px">LOREM IPSUM DOLOR</div>
    <div class="photo" style="left:259px;top:84px;width:74px;height:45px;background:linear-gradient(120deg,#d7dde0,#a9b7bd)" role="img" aria-label="Nurse caring for a patient"></div>
    <div class="photo" style="left:28px;top:129px;width:74px;height:45px;background:linear-gradient(120deg,#e3e6e8,#b9c3c8)" role="img" aria-label="Doctor consulting with a patient"></div>
    <div class="tile g" style="left:102px;top:129px;width:78px;height:45px">LOREM IPSUM DOLOR</div>
    <div class="tile t" style="left:180px;top:129px;width:153px;height:45px">Lorem ipsum dolor sit amet, consectetur adipiscing elit, sed do eiusmod tempor incididunt ut labore et dolore magna aliqua. Ut enim ad minim veniam, quis nostrud exercitation</div>
    <div class="foot-brand brand"><span class="mark"></span>Tall FERN</div>
    <div class="foot-line"></div><div class="foot-tab">03</div>
  </section>

  <!-- About us: columns -->
  <section class="slide about-c c2 r2">
    <div class="title">ABOUT US</div>
    <div class="photo" style="left:26px;top:46px;width:64px;height:45px;background:linear-gradient(120deg,#eceff1,#c7cfd3)" role="img" aria-label="Doctor and patients reviewing results"></div>
    <p class="cap">Lorem ipsum dolor sit amet consectetur adipiscing elitsed do eiusmod</p>
    <div class="col body" style="left:100px">
      <p>Lorem ipsum dolor sit amet, consectetur adipiscing elit, sed do eiusmod tempor incididunt ut labore et dolore magna aliqua. Ut enim ad minim veniam, quis nostrud exercitation ullamco laboris nisi ut aliquip ex ea commodo consequat. Duis aute irure dolor in reprehenderit in voluptate velit esse cillum dolore eu fugiat nulla pariatur.</p>
      <p>Lorem ipsum dolor sit amet, consectetur adipiscing elit, sed do eiusmod tempor incididunt ut labore et dolore magna aliqua. Ut enim ad minim veniam, quis nostrud exercitation ullamco laboris nisi ut aliquip ex ea commodo</p>
    </div>
    <div class="col body" style="left:226px">
      <p>Lorem ipsum dolor sit amet, consectetur adipiscing elit, sed do eiusmod tempor incididunt ut labore et dolore magna aliqua. Ut enim ad minim veniam, quis nostrud exercitation ullamco laboris nisi ut aliquip ex ea commodo consequat. Duis aute irure dolor in reprehenderit in voluptate velit esse cillum dolore eu fugiat nulla pariatur.</p>
      <p>Lorem ipsum dolor sit amet, consectetur adipiscing elit, sed do eiusmod tempor incididunt ut labore et dolore magna aliqua. Ut enim ad minim veniam, quis nostrud exercitation ullamco laboris nisi ut aliquip ex ea commodo</p>
    </div>
    <div class="foot-brand brand"><span class="mark"></span>Tall FERN</div>
    <div class="foot-line"></div><div class="foot-tab">04</div>
  </section>

  <!-- Market condition -->
  <section class="slide market c3 r2">
    <div class="title">MARKET CONDITION</div>
    <svg class="abs" style="left:0;top:0" width="362" height="203">
      <g transform="rotate(-90 128 130)" fill="none" stroke-width="16">
        <circle cx="128" cy="130" r="44" stroke="var(--green)" stroke-dasharray="160.3 276.5"/>
        <circle cx="128" cy="130" r="44" stroke="var(--green-dark)" stroke-dasharray="0 161.3 31.2 276.5"/>
        <circle cx="128" cy="130" r="44" stroke="var(--gray)" stroke-dasharray="0 193.5 34.9 276.5"/>
        <circle cx="128" cy="130" r="44" stroke="var(--green-dark)" stroke-dasharray="0 229.4 45.9 276.5"/>
      </g>
      <g fill="var(--green-dark)">
        <circle cx="128" cy="109" r="4"/>
        <rect x="122" y="114" width="12" height="17" rx="2"/>
        <rect x="123.5" y="129" width="4" height="16"/>
        <rect x="128.5" y="129" width="4" height="16"/>
      </g>
      <g stroke="var(--gray)" stroke-width=".6" fill="none">
        <polyline points="67,305 67,307"/>
        <polyline points="69,67 69,75 108,75"/>
        <polyline points="50,98 50,103 80,103"/>
        <polyline points="54,158 54,149 88,149"/>
        <polyline points="210,98 210,122 172,122"/>
      </g>
      <g fill="var(--gray)"><circle cx="69" cy="75" r="1"/><circle cx="50" cy="103" r="1"/><circle cx="54" cy="149" r="1"/><circle cx="210" cy="98" r="1"/></g>
    </svg>
    <div class="pct" style="left:44px;top:56px">17%</div>
    <div class="pct" style="left:35px;top:85px;color:var(--gray)">13%</div>
    <div class="pct" style="left:51px;top:158px">12%</div>
    <div class="pct" style="left:190px;top:62px;font-size:15px;color:var(--green)">58%</div>
    <p class="side body"><span class="lead">Lorem ipsum dolor sit amet,</span><br>consectetur adipiscing elit, sed do eiusmod tempor incididunt ut labore et dolore magna aliqua. Ut enim ad minim veniam, quis nostrud exercitation ullamco laboris nisi ut aliquip ex ea commodo consequat. Duis aute irure dolor in reprehenderit in voluptate velit esse cillum</p>
    <div class="foot-brand brand"><span class="mark"></span>Tall FERN</div>
    <div class="foot-line"></div><div class="foot-tab">05</div>
  </section>

  <!-- Bar chart -->
  <section class="slide chart c1 r3">
    <div class="title">OUR CHART</div>
    <svg class="abs" style="left:0;top:0" width="362" height="203">
      <g stroke="#9a9a9a" stroke-width=".6">
        <line x1="87" y1="40" x2="87" y2="138"/>
        <line x1="87" y1="138" x2="300" y2="138"/>
        <line x1="85" y1="58" x2="87" y2="58"/><line x1="85" y1="78" x2="87" y2="78"/>
        <line x1="85" y1="98" x2="87" y2="98"/><line x1="85" y1="118" x2="87" y2="118"/>
      </g>
      <g>
        <rect x="93" y="67" width="9" height="71" fill="var(--green)"/>
        <rect x="102" y="98" width="9" height="40" fill="var(--gray-light)"/>
        <rect x="111" y="104" width="9" height="34" fill="var(--green-dark)"/>
        <rect x="134" y="86" width="9" height="52" fill="var(--green)"/>
        <rect x="143" y="67" width="9" height="71" fill="var(--gray-light)"/>
        <rect x="152" y="104" width="9" height="34" fill="var(--green-dark)"/>
        <rect x="176" y="73" width="9" height="65" fill="var(--green)"/>
        <rect x="185" y="106" width="9" height="32" fill="var(--gray-light)"/>
        <rect x="194" y="92" width="9" height="46" fill="var(--green-dark)"/>
        <rect x="218" y="76" width="9" height="62" fill="var(--green)"/>
        <rect x="227" y="99" width="9" height="39" fill="var(--gray-light)"/>
        <rect x="236" y="69" width="9" height="69" fill="var(--green-dark)"/>
      </g>
      <g font-size="2.6" fill="#fff" font-family="Open Sans, sans-serif" text-anchor="middle">
        <rect x="141" y="58" width="10" height="5" fill="var(--gray-light)"/><text x="146" y="61.6">70%</text>
        <rect x="176" y="64" width="10" height="5" fill="var(--green)"/><text x="181" y="67.6">65%</text>
        <rect x="194" y="83" width="10" height="5" fill="var(--green-dark)"/><text x="199" y="86.6">46%</text>
      </g>
    </svg>
    <div class="year" style="left:101px">2009</div>
    <div class="year" style="left:142px">2010</div>
    <div class="year" style="left:184px">2011</div>
    <div class="year" style="left:226px">2012</div>
    <div class="legend" style="left:64px"><b><i style="background:var(--green)"></i>LOREM IPSUM</b>Lorem ipsum dolor sit amet, consectetur adipiscing elit, sed do eiusmod tempor incididunt ut labore et dolore magna</div>
    <div class="legend" style="left:142px"><b><i style="background:var(--gray-light)"></i>LOREM IPSUM</b>Lorem ipsum dolor sit amet, consectetur adipiscing elit, sed do eiusmod tempor incididunt ut labore et dolore magna</div>
    <div class="legend" style="left:221px"><b><i style="background:var(--green-dark)"></i>LOREM IPSUM</b>Lorem ipsum dolor sit amet, consectetur adipiscing elit, sed do eiusmod tempor incididunt ut labore et dolore magna</div>
    <div class="foot-brand brand"><span class="mark"></span>Tall FERN</div>
    <div class="foot-line"></div><div class="foot-tab">06</div>
  </section>

  <!-- Ring charts -->
  <section class="slide c2 r3">
    <div class="title">OUR CHART</div>
    <svg class="abs" style="left:0;top:0" width="362" height="203">
      <g fill="none" stroke-width="5">
        <circle cx="80" cy="88" r="21" stroke="var(--gray)"/>
        <circle cx="80" cy="88" r="21" stroke="var(--green)" stroke-dasharray="106.9 132" transform="rotate(-90 80 88)"/>
        <circle cx="185" cy="88" r="21" stroke="var(--gray)"/>
        <circle cx="185" cy="88" r="21" stroke="var(--green)" stroke-dasharray="95 132" transform="rotate(-90 185 88)"/>
        <circle cx="287" cy="88" r="21" stroke="var(--gray)"/>
        <circle cx="287" cy="88" r="21" stroke="var(--green)" stroke-dasharray="83.2 132" transform="rotate(-90 287 88)"/>
      </g>
      <g font-family="Open Sans, sans-serif" font-size="9" font-weight="600" fill="var(--green-dark)" text-anchor="middle">
        <text x="80" y="91">81%</text><text x="185" y="91">72%</text><text x="287" y="91">63%</text>
      </g>
    </svg>
    <p class="ring-note" style="left:40px">dolor sit amet, consectetur adipiscing elit, sed do eiusmod tempor incididunt ut labore et dolore magna aliqua. Ut enim ad minim veniam, quis nostrud exercitation ullamco laboris nisi ut aliquip ex ea commodo fugiat nulla pariatur.</p>
    <p class="ring-note" style="left:145px">dolor sit amet, consectetur adipiscing elit, sed do eiusmod tempor incididunt ut labore et dolore magna aliqua. Ut enim ad minim veniam, quis nostrud exercitation ullamco laboris nisi ut aliquip ex ea commodo fugiat nulla pariatur.</p>
    <p class="ring-note" style="left:247px">dolor sit amet, consectetur adipiscing elit, sed do eiusmod tempor incididunt ut labore et dolore magna aliqua. Ut enim ad minim veniam, quis nostrud exercitation ullamco laboris nisi ut aliquip ex ea commodo fugiat nulla pariatur.</p>
    <div class="foot-brand brand"><span class="mark"></span>Tall FERN</div>
    <div class="foot-line"></div><div class="foot-tab">07</div>
  </section>

  <!-- Services -->
  <section class="slide c3 r3">
    <div class="title">OUR SERVICES</div>
    <div class="svc" style="left:54px">
      <div class="top" style="background:var(--green)">
        <svg width="22" height="22" viewBox="0 0 22 22"><path d="M11 2 L20 11 L11 20 L2 11 Z" fill="#fff"/><circle cx="11" cy="11" r="3" fill="var(--green)"/></svg>
      </div>
      <p>Dolor sit amet, consectetur adipiscing elit, sed do eiusmod tempor incididunt ut labore et dolore magna aliqua.</p>
    </div>
    <div class="svc" style="left:142px">
      <div class="top" style="background:#7a7a7a">
        <svg width="22" height="22" viewBox="0 0 22 22" fill="none" stroke="#fff" stroke-width="2"><circle cx="11" cy="12.5" r="7.5"/><line x1="11" y1="12.5" x2="11" y2="8"/><line x1="8.5" y1="2.5" x2="13.5" y2="2.5"/></svg>
      </div>
      <p>Dolor sit amet, consectetur adipiscing elit, sed do eiusmod tempor incididunt ut labore et dolore magna aliqua.</p>
    </div>
    <div class="svc" style="left:229px">
      <div class="top" style="background:var(--green)">
        <svg width="22" height="22" viewBox="0 0 22 22" fill="#fff"><rect x="3" y="12" width="4" height="8"/><rect x="9" y="9" width="4" height="11"/><rect x="15" y="6" width="4" height="14"/><path d="M3 9 L11 3 L10 1.5 L15 1.5 L13.5 6 L12.3 4.6 L4 10.6 Z"/></svg>
      </div>
      <p>Dolor sit amet, consectetur adipiscing elit, sed do eiusmod tempor incididunt ut labore et dolore magna aliqua.</p>
    </div>
    <div class="foot-brand brand"><span class="mark"></span>Tall FERN</div>
    <div class="foot-line"></div><div class="foot-tab">08</div>
  </section>

  <!-- Image text -->
  <section class="slide imgtext c1 r4">
    <div class="photo" style="left:155px;top:0;width:207px;height:203px;background:linear-gradient(90deg,#dfe9f2 0%,#6fa6d8 40%,#1f64b4 75%,#cfdceb 100%)" role="img" aria-label="Laboratory test tubes with blue liquid and a pipette"></div>
    <div class="left"></div>
    <h3>IMAGE TEXT</h3>
    <p class="body">Lorem ipsum dolor sit amet, consectetur adipiscing elit, sed do eiusmod tempor incididunt ut labore et dolore magna aliqua. Ut enim ad minim veniam, quis nostrud exercitation ullamco laboris nisi ut aliquip ex ea commodo consequat. Duis aute irure dolor in reprehenderit in voluptate velit esse cillum dolore eu fugiat nulla pariatur.</p>
    <div class="foot-brand brand"><span class="mark"></span>Tall FERN</div>
  </section>

  <!-- Section title -->
  <section class="slide section c2 r4" role="img" aria-label="Green microscopic cells and virus particles background">
    <div class="icon">i</div>
    <div class="line"></div>
    <h4>SECTION TITLE</h4>
  </section>

  <!-- Contact -->
  <section class="slide contact c3 r4">
    <div class="brand"><span class="mark"></span>Tall FERN</div>
    <div class="photo" style="left:0;top:82px;width:362px;height:91px;background:linear-gradient(100deg,#e8ebee 0%,#dfe4ea 35%,#bcd2ea 55%,#e7eaed 75%,#e2e6ea 100%)" role="img" aria-label="Street map showing the office location"></div>
    <div class="info">
      <span><i></i>4120 Willow Crest Road Ste 210</span>
      <span><i></i>support@tallfern.com</span>
      <span><i></i>www.tallfern.com</span>
    </div>
  </section>

</main>
</body>
</html>
```